General Contractors need a new Crisp updated Card Design

We need a new business card design for our company of 25 years based in Toronto call Holvaster Building Inc. : Our goal is to be the leading commercial contractors in Toronto by providing exceptional value to our clients. We work very hard to deliver professional, quality, service in conjunction with consistent price competitiveness to all of our clients on every single project.

Target Market(s)

Design & Build Clients

Industry/Entity Type

Construction Company

Contact Information for Business Card

Address:
18 North Tamlin Glen Road, Unit 57, Marbrook Vale, ON, K7T 2R9
Office: 905-218-5937

Holvasters Logo
Employee Job Description
Employee Cell Phone #
Employee Email
www.holvaster-example.com

Colors

Designer to choose colors to be used in the design.

Requirements
Must have
• Quote Company Saying:
• "Professional. Quality. Service."
Nice to have
• New Crisp up to date look. simple & fresh ( Not to Busy)
Should not have
• NO BLUE PRINTS ON THE BUSINESS CARDS

```html
<!DOCTYPE html>
<html lang="en">
<head>
<meta charset="utf-8">
<title>Holvaster Building Inc. – Business Card</title>
<link rel="stylesheet" href="https://fonts.googleapis.com/css2?family=EB+Garamond:wght@500;700&family=Cinzel:wght@400&display=swap">
<style>
  :root {
    --brand-green: #00695b;
    --brand-green-dark: #005a4e;
    --tagline-green: #86ad a2;
    --tagline: #8fb3a8;
    --paper: #fbfbf9;
    --backdrop: #d9dbdb;
  }
  * { margin: 0; padding: 0; box-sizing: border-box; }
  html, body {
    width: 1200px; height: 1200px; overflow: hidden;
    background: var(--backdrop);
    font-family: "EB Garamond", Georgia, serif;
  }
  .sheet {
    width: 1200px; height: 1200px;
    display: flex; flex-direction: column;
    align-items: center; justify-content: center; gap: 60px;
  }
  .card {
    width: 840px; height: 480px; position: relative;
    box-shadow: 0 6px 18px rgba(0,0,0,0.18);
  }
  /* Brand lockup */
  .brand { display: flex; align-items: center; gap: 18px; }
  .brand-square { width: 62px; height: 62px; flex: none; }
  .brand-name {
    font-weight: 700; font-size: 34px; line-height: 1.0;
    letter-spacing: 0.02em; text-transform: uppercase;
  }
  /* Front (contact side) */
  .card-front { background: var(--paper); color: var(--brand-green); }
  .card-front .brand { position: absolute; left: 200px; top: 50px; }
  .card-front .brand-square { background: var(--brand-green); }
  .address {
    position: absolute; left: 70px; top: 200px;
    font-weight: 700; font-size: 25px; line-height: 1.2;
    font-style: normal;
  }
  .person { position: absolute; left: 520px; top: 190px; }
  .person-name { font-weight: 700; font-size: 38px; line-height: 1.1; }
  .person-title { font-weight: 500; font-size: 19px; }
  .contact-list {
    position: absolute; left: 470px; top: 312px; list-style: none;
    font-weight: 700; font-size: 23px;
  }
  .contact-list li { display: flex; align-items: center; gap: 16px; height: 36px; }
  .contact-badge {
    width: 26px; height: 26px; background: var(--brand-green); color: var(--paper);
    font-size: 17px; display: flex; align-items: center; justify-content: center;
  }
  /* Back (brand side) */
  .card-back {
    background: var(--brand-green); color: var(--paper);
    display: flex; flex-direction: column; align-items: center; justify-content: center;
    gap: 48px;
  }
  .card-back .brand-square { background: var(--paper); }
  .card-back .brand-name { font-size: 40px; }
  .card-back .brand-square { width: 72px; height: 72px; }
  .tagline {
    font-family: "Cinzel", "Times New Roman", serif;
    font-size: 27px; letter-spacing: 0.16em; color: var(--tagline);
  }
</style>
</head>
<body>
<main class="sheet">
  <section class="card card-front" aria-label="Business card, contact side">
    <div class="brand">
      <span class="brand-square" aria-hidden="true"></span>
      <span class="brand-name">Holvaster<br>Building Inc.</span>
    </div>
    <address class="address">
      18 North Tamlin Glen Road,<br>
      Unit 57, Marbrook Vale,<br>
      ON, K7T 2R9<br>
      Office: 905-218-5937
    </address>
    <div class="person">
      <p class="person-name">Marcus Ellery</p>
      <p class="person-title">Marketing Executive</p>
    </div>
    <ul class="contact-list">
      <li><span class="contact-badge">P</span>0002 004 017</li>
      <li><span class="contact-badge">E</span>executive@holvaster-example.com</li>
      <li><span class="contact-badge">W</span>www.holvaster-example.com</li>
    </ul>
  </section>

  <section class="card card-back" aria-label="Business card, brand side">
    <div class="brand">
      <span class="brand-square" aria-hidden="true"></span>
      <span class="brand-name">Holvaster<br>Building Inc.</span>
    </div>
    <p class="tagline">PROFESSIONAL. QUALITY. SERVICE.</p>
  </section>
</main>
</body>
</html>
```